VORALUX SYSTEMS BUSINESS CARD DESIGN

WE WANT COMPLETE NEW DESIGN OF OUR BUSINESS CARD. WE ARE AN INTEGRATION COMPANY, WHERE WE INTEGRATE IOT/SMART SYSTEMS TO HOMES AND CORPORATE CUSTOMERS. WE SUPPLY AND INSTALL AUTOMATION PRODUCTS. THE FINAL DESIGN SHOULD COMMUNICATE TECHNOLOGY. THE CARD DESIGN SHOULD BE VERY IMPACT FULL. LOGO NEEDS TO BE THERE. IT WOULD NICE IF THE DESIGN WAS CLEAN. COLORS IS UP TO DESIGNER TO PLAY WITH, OR CAN STICK TO CORPORATE COLORS (FOLLOW LOGO). I HAVE ADDED FEW REFERENCE PHOTOS TO DRAW INSPIRATION MAYBE. I HAVE ADDED A HEX DESIGN, ITS NOT NECESSARY TO USE THIS DESIGN, ITS UPTO DESIGNER, JUST ADDED IF NEEDED TO PLAY WITH DESIGN.

Target Market(s)

Private end users and corporate clients

Industry/Entity Type

technology, home automation, home theaters, building management systems, IOT

Contact Information for Business Card

It should include Employee name, personal number, office number, email address, both in English and arabic. DETAILS TO INCLUDE :DANIEL MARUVEN, MOBILE 0097150738219,OFFCIE 009714368174, DANIEL@VORALUXSYS.CO

Requirements
Must have
• Should feel like a technology company from design. Details both and in English and arabic (or at least have provision for arabic in design).
Nice to have
• I would like logo on one side, and details on the other side. Logo design side should communicate technology with logo. Other side can be clean just with information or also have some design aspects following from logo side. it would be interesting to see submissions with square design as well (that looks like an app Icon). colors could be of logo, red black grey and white. I have added some designs to draw inspiration from

```html
<!DOCTYPE html>
<html lang="en">
<head>
<meta charset="utf-8">
<title>Voralux Systems Business Card</title>
<link rel="stylesheet" href="https://fonts.googleapis.com/css2?family=Montserrat:wght@600;800&family=Open+Sans:wght@400;600&family=Cairo:wght@400;700&display=swap">
<style>
  :root {
    --stage: #c9c9c9;
    --card-dark: #1c1c1c;
    --trace-dark: #2a2a2a;
    --card-light: #ffffff;
    --ink: #151515;
    --grey: #9a9a9a;
    --grey-soft: #ececec;
    --red: #e3262b;
    --white: #ffffff;
  }
  * { margin: 0; padding: 0; box-sizing: border-box; }
  html, body { width: 1200px; height: 900px; overflow: hidden; }
  body {
    background: var(--stage);
    position: relative;
    font-family: "Open Sans", sans-serif;
  }
  .card {
    position: absolute;
    width: 560px;
    height: 320px;
    border-radius: 26px;
    overflow: hidden;
    box-shadow: 0 10px 24px rgba(0,0,0,0.25);
  }
  .card--front { left: 60px; top: 90px; background: var(--card-dark); }
  .card--back { left: 580px; top: 490px; background: var(--card-light); }

  .traces { position: absolute; inset: 0; width: 100%; height: 100%; }

  .brand { display: flex; align-items: center; gap: 14px; }
  .brand__dot {
    width: 26px; height: 26px;
    border-radius: 50%;
    background: var(--red);
    flex: none;
  }
  .brand__name {
    font-family: "Montserrat", sans-serif;
    font-weight: 800;
    letter-spacing: 0.04em;
    white-space: nowrap;
  }
  .arabic {
    font-family: "Cairo", sans-serif;
    direction: rtl;
  }

  .front__lockup {
    position: absolute;
    left: 0; right: 0; top: 82px;
    display: flex;
    flex-direction: column;
    align-items: center;
    gap: 8px;
  }
  .front__lockup .brand__name { color: var(--white); font-size: 36px; }
  .front__legal {
    font-family: "Montserrat", sans-serif;
    font-weight: 600;
    font-size: 16px;
    letter-spacing: 0.12em;
    color: var(--grey);
  }
  .front__tagline {
    font-family: "Montserrat", sans-serif;
    font-weight: 600;
    font-size: 13px;
    letter-spacing: 0.3em;
    color: var(--white);
  }
  .front__arabic {
    font-size: 18px;
    font-weight: 700;
    color: var(--grey);
    margin-top: 4px;
  }

  .back__band {
    position: absolute;
    right: -40px; top: -40px;
    width: 300px; height: 400px;
    background: var(--grey-soft);
    transform: skewX(-18deg);
  }
  .back__brand { position: absolute; left: 40px; top: 40px; }
  .back__brand .brand__name { color: var(--ink); font-size: 28px; }
  .back__legal {
    position: absolute; left: 80px; top: 78px;
    font-family: "Montserrat", sans-serif;
    font-weight: 600;
    font-size: 13px;
    letter-spacing: 0.1em;
    color: var(--grey);
  }
  .person {
    position: absolute; left: 40px; top: 150px;
    font-family: "Montserrat", sans-serif;
    font-weight: 800;
    font-size: 21px;
    letter-spacing: 0.02em;
    color: var(--ink);
  }
  .person__arabic {
    position: absolute; left: 40px; top: 180px;
    font-size: 16px;
    font-weight: 700;
    color: var(--grey);
    direction: ltr;
  }
  .contact {
    position: absolute;
    list-style: none;
    font-size: 14px;
    color: var(--ink);
    display: flex;
    flex-direction: column;
    gap: 6px;
  }
  .contact li { display: flex; align-items: center; gap: 8px; white-space: nowrap; }
  .contact svg { width: 15px; height: 15px; flex: none; }
  .contact--phones { left: 40px; bottom: 34px; }
  .contact--online { right: 30px; bottom: 34px; align-items: flex-end; }
  .contact__label { font-family: "Cairo", sans-serif; font-size: 12px; color: var(--grey); }
</style>
</head>
<body>

  <section class="card card--front" aria-label="Card front">
    <svg class="traces" viewBox="0 0 560 320" aria-hidden="true">
      <g fill="none" stroke="var(--trace-dark)" stroke-width="3">
        <path d="M0 270 H150 L190 230 H330"/>
        <path d="M560 60 H430 L390 100 H300"/>
        <path d="M560 250 H460 L420 290 H360"/>
        <path d="M0 40 H90 L120 70"/>
      </g>
      <g fill="var(--trace-dark)">
        <circle cx="330" cy="230" r="6"/>
        <circle cx="300" cy="100" r="6"/>
        <circle cx="360" cy="290" r="6"/>
        <circle cx="120" cy="70" r="6"/>
      </g>
    </svg>
    <div class="front__lockup">
      <div class="brand">
        <span class="brand__dot"></span>
        <span class="brand__name">VORALUX SYSTEMS</span>
      </div>
      <p class="front__legal">L.L.C</p>
      <p class="front__tagline">A VORALUX GROUP DIVISION.</p>
      <p class="arabic front__arabic">فورالوكس سيستمز ذ.م.م</p>
    </div>
  </section>

  <section class="card card--back" aria-label="Card back">
    <div class="back__band"></div>
    <svg class="traces" viewBox="0 0 560 320" aria-hidden="true">
      <g fill="none" stroke="var(--white)" stroke-width="4">
        <path d="M560 120 H440 L400 160 H330"/>
        <path d="M560 200 H470 L440 230"/>
      </g>
      <g fill="var(--white)">
        <circle cx="330" cy="160" r="7"/>
        <circle cx="440" cy="230" r="7"/>
      </g>
    </svg>
    <div class="brand back__brand">
      <span class="brand__dot"></span>
      <span class="brand__name">VORALUX SYSTEMS</span>
    </div>
    <p class="back__legal">L.L.C</p>

    <h1 class="person">DANIEL MARUVEN</h1>
    <p class="arabic person__arabic">دانيال ماروفين</p>

    <ul class="contact contact--phones">
      <li>
        <svg viewBox="0 0 16 16" aria-hidden="true"><path fill="none" stroke="var(--red)" stroke-width="1.8" d="M4 2l2.5 3-1.5 1.5a8 8 0 0 0 4.5 4.5L11 9.5l3 2.5-1.5 2C7 14 2 9 2 3.5z"/></svg>
        0097150738219 <span class="contact__label">جوال</span>
      </li>
      <li>
        <svg viewBox="0 0 16 16" aria-hidden="true"><rect x="4" y="1.5" width="8" height="13" rx="1.5" fill="none" stroke="var(--red)" stroke-width="1.6"/><circle cx="8" cy="12" r="0.9" fill="var(--red)"/></svg>
        009714368174 <span class="contact__label">مكتب</span>
      </li>
    </ul>

    <ul class="contact contact--online">
      <li>
        DANIEL@VORALUXSYS.CO
        <svg viewBox="0 0 16 16" aria-hidden="true"><rect x="1" y="3.5" width="14" height="9" fill="var(--red)"/><path d="M1 3.5l7 5 7-5" fill="none" stroke="var(--white)" stroke-width="1.2"/></svg>
      </li>
      <li>
        WWW.VORALUXSYS.COM
        <svg viewBox="0 0 16 16" aria-hidden="true"><circle cx="8" cy="8" r="6.5" fill="var(--red)"/><path d="M1.5 8h13M8 1.5c-3 3.5-3 9.5 0 13M8 1.5c3 3.5 3 9.5 0 13" fill="none" stroke="var(--white)" stroke-width="1"/></svg>
      </li>
    </ul>
  </section>

</body>
</html>
```